rt for guide - bartholomew finch personal speaking/consulting website

custom website for my personal speaking/consulting services brand, you can see the basic site we are using as a placeholder at www.rtforguide.example now. I want to re-position this to more of a personal brand site and have video samples of speaking events, downloadable content, a video blog, and links to podcast. I really like the design of dorianwelk.example and the feature set should be fairly similar to his. I'll begin to compile more stock images etc. to use for sliders like he has done, for now we'll need to use stock imagery or existing photography from my social accounts. You can get a feel for social at all platforms/bfinchbroker i.e. facebook.com/bfinchbroker. the site should be primarily geared toward showcasing speaking/consulting services and content, as well as be flexible to allow for additional downloadables etc. in the future.

Target Market(s)

entrepreneurs and leaders looking to grow themselves, their business, and those they lead.

Coding

Coded - Design and coding required

Number of Pages Required

3 page

Font styles to use
Sans Serif

Colors

Designer to choose colors to be used in the design.

Requirements
Must have
• modern slick design, video blog, podcast feed, registration for people to subscribe to newsletter

```html
<!DOCTYPE html>
<html lang="en">
<head>
<meta charset="utf-8">
<title>RT for Guide — Bartholomew Finch</title>
<link href="https://fonts.googleapis.com/css2?family=Nunito:wght@400;600;700;800&display=swap" rel="stylesheet">
<style>
:root{
  --orange:#ef6340;
  --blue:#1b8fd9;
  --red:#c8161d;
  --ink:#222;
  --muted:#666;
  --grey-band:#f3f3f3;
  --footer:#1f2226;
  --white:#fff;
}
*{box-sizing:border-box;margin:0;padding:0}
html,body{width:1200px;height:3457px;overflow:hidden}
body{font-family:'Nunito',sans-serif;color:var(--ink);background:var(--white);position:relative}
.abs{position:absolute}
.photo{position:absolute;display:block}
.accent{color:var(--orange)}
.hl{color:var(--blue)}

/* hero */
.hero{position:absolute;left:0;top:0;width:1200px;height:597px;
  background:linear-gradient(180deg,#6b5a7d 0%,#c9826a 28%,#8a6a52 55%,#4a4a35 80%,#3d3b2c 100%)}
.hero-person{position:absolute;left:640px;top:150px;width:430px;height:447px;
  background:linear-gradient(180deg,#7a6050 0%,#2d5fa8 45%,#244f91 100%);border-radius:200px 200px 0 0}
.brand{position:absolute;left:142px;top:18px;display:flex;align-items:center;gap:10px;color:var(--white);font-weight:800;font-size:26px}
.brand-dot{width:26px;height:26px;border-radius:50%;background:var(--white)}
.phone{position:absolute;left:786px;top:22px;display:flex;align-items:center;gap:10px;color:var(--white);font-size:20px;font-weight:600}
.menu{position:absolute;left:1029px;top:17px;width:36px;height:36px;border:2px solid var(--white);border-radius:50%}
.menu i{position:absolute;left:9px;width:15px;height:2px;background:var(--white)}
.hero-title{position:absolute;left:145px;top:300px;color:var(--white);font-size:38px;font-weight:800;line-height:50px;text-shadow:0 2px 4px rgba(0,0,0,.5)}
.btn-red{position:absolute;left:142px;top:467px;width:227px;height:38px;background:var(--red);color:var(--white);font-size:17px;font-weight:700;display:flex;align-items:center;justify-content:center}

/* subscribe */
.sub-title{position:absolute;left:0;top:744px;width:1200px;text-align:center;font-size:30px;font-weight:700;line-height:40px}
.sub-text{position:absolute;left:170px;top:836px;width:860px;text-align:center;font-size:17px;line-height:27px}
.field{position:absolute;top:915px;width:326px;height:41px;border:1px solid #cfcfcf;border-radius:21px;font-size:13px;color:#888;padding:0 19px;display:flex;align-items:center}
.pill{position:absolute;height:33px;border-radius:17px;background:var(--blue);color:var(--white);font-size:14px;font-weight:700;display:flex;align-items:center;justify-content:center;gap:6px;box-shadow:0 3px 6px rgba(27,143,217,.35)}

/* about */
.about-band{position:absolute;left:0;top:1161px;width:1200px;height:443px;background:var(--grey-band)}
.about-photo{left:142px;top:1127px;width:392px;height:403px;background:radial-gradient(circle at 50% 45%,#9a7a62 0%,#5b6146 45%,#2f3a2c 100%)}
.about-title{position:absolute;left:595px;top:1228px;font-size:30px;font-weight:700}
.about-lead{position:absolute;left:595px;top:1280px;width:470px;font-size:13px;line-height:21px;color:#222}
.about-body{position:absolute;left:595px;top:1330px;width:470px;font-size:13px;line-height:20.5px;color:var(--muted)}

/* services */
.section-title{position:absolute;left:0;width:1200px;text-align:center;font-size:30px;font-weight:700}
.service{position:absolute;top:1747px;height:330px}
.service-title{position:absolute;left:35px;top:245px;color:var(--white);font-size:19px;font-weight:700}
.service-text{position:absolute;left:35px;top:272px;width:310px;color:var(--white);font-size:13px;line-height:19px}
.service-arrow{position:absolute;right:22px;top:240px}

/* videos */
.video{position:absolute;top:2216px;height:327px}
.play{position:absolute;top:95px;width:90px;height:90px}
.video-cap{position:absolute;left:37px;top:270px;color:var(--white);font-size:14px;font-weight:700}
.video-date{position:absolute;left:37px;top:295px;color:var(--white);font-size:13px}

/* feature cards */
.feature{position:absolute;top:2700px;width:296px;height:380px}
.feature .photo{left:0;top:0;width:296px;height:214px}
.feature-body{position:absolute;left:0;top:214px;width:296px;height:166px;color:var(--white);text-align:center}
.feature-body h3{font-size:21px;font-weight:700;margin-top:24px}
.feature-body p{font-size:13px;line-height:19px;margin:12px 18px 0}
.plus{position:absolute;left:129px;top:146px;width:38px;height:38px;border-radius:50%;background:var(--white);color:#999;font-size:14px;display:flex;justify-content:center;padding-top:3px}
.bg-blue{background:var(--blue)}
.bg-orange{background:var(--orange)}

/* footer */
.footer{position:absolute;left:0;top:3177px;width:1200px;height:280px;background:linear-gradient(180deg,#1c1f24,#24272b)}
.footer-text{position:absolute;left:142px;top:58px;width:340px;color:#ddd;font-size:13px;line-height:20px}
.footer-input{position:absolute;left:142px;top:119px;width:372px;height:46px;border-radius:23px;background:var(--white)}
.footer-input span{position:absolute;left:24px;top:15px;font-size:12px;color:#444}
.footer-input b{position:absolute;right:0;top:0;width:158px;height:46px;border-radius:23px;background:var(--blue);color:var(--white);font-size:15px;font-weight:700;display:flex;align-items:center;justify-content:center;letter-spacing:.5px}
.footer-links{position:absolute;left:573px;top:58px;list-style:none;color:#ddd;font-size:12px}
.footer-links li{height:32px}
.footer-links li::before{content:"›";color:var(--blue);margin-right:8px}
.contact{position:absolute;left:707px;color:#ddd;font-size:12px;line-height:17px}
.contact-ico{position:absolute;left:707px}
.footer-brand{position:absolute;left:917px;top:82px;color:var(--white);font-size:21px;font-weight:800}
.social{position:absolute;top:128px;width:30px;height:30px;border:1px solid #555}
.rule{position:absolute;left:142px;top:228px;width:916px;height:1px;background:#3a3d41}
.copy{position:absolute;left:0;top:248px;width:1200px;text-align:center;color:#bbb;font-size:12px}
</style>
</head>
<body>

<header class="hero" role="img" aria-label="City skyline at sunset with mountains behind it">
  <div class="hero-person" role="img" aria-label="Portrait of the coach in a blue polo shirt"></div>
  <div class="brand"><span class="brand-dot"></span>RT for Guide</div>
  <div class="phone">
    <svg width="26" height="26" viewBox="0 0 24 24" fill="none" stroke="#fff" stroke-width="1.5"><path d="M5 3h4l2 5-3 2a11 11 0 0 0 6 6l2-3 5 2v4a2 2 0 0 1-2 2A17 17 0 0 1 3 5a2 2 0 0 1 2-2z"/></svg>
    +(00) 555 010 2468
  </div>
  <div class="menu"><i style="top:11px"></i><i style="top:16px"></i><i style="top:21px"></i></div>
  <h1 class="hero-title">The Place Where<br>Entrepreneurs Come To<br>Become Leaders.</h1>
  <div class="btn-red">Contact Me Today</div>
</header>

<section>
  <h2 class="sub-title"><span class="accent">Subscribe To This Blog To Get The Latest Tips And Tricks</span><br><span class="accent">To Help You Be A</span> <span class="hl">Successful Entrepreneur</span></h2>
  <p class="sub-text">Bartholomew Finch and Marcus Delvane swap their secrets on how to polish your leadership skills, shift your business mindset, and empower your team.</p>
  <div class="field" style="left:252px">Enter Your Name</div>
  <div class="field" style="left:595px">Enter Your Email Address</div>
  <div class="pill" style="left:487px;top:1000px;width:234px">Subscribe To Our Podcast <span>⟶</span></div>
</section>

<section>
  <div class="about-band"></div>
  <div class="photo about-photo" role="img" aria-label="Portrait of Bartholomew Finch in an office"></div>
  <h2 class="about-title"><span class="accent">About</span> <span class="hl">Bartholomew Finch</span></h2>
  <p class="about-lead">Lorem ipsum dolor sit amet, consectetuer adipiscing elit, sed diamonummy nibh euismod tincidunt ut laoreet dolore magna aliquam erat volutpat.</p>
  <p class="about-body">Ut wisi enim ad minim veniam, quis nostrud exerci tation ullamcorperuscipit lobortis nisl ut aliquip ex ea commodo consequat. Duis autem vel eum iriure dolor in hendrerit in vulputate velit esse molestie consequat, vel illum dolore eu feugiat nulla facilisis at vero eros et accumsan et iusto odio dignissimui blandit praesent luptatum zzril delenit augue duis dolore te feugait nullalisi. Morbi id sapien vel ex posuere congue vitae cursus nulla.</p>
  <div class="pill" style="left:595px;top:1483px;width:126px;height:31px">Read More <span>⟶</span></div>
</section>

<section>
  <h2 class="section-title" style="top:1688px"><span class="accent">Our</span> <span class="hl">Services For</span></h2>
  <div class="service" style="left:0;width:396px;background:linear-gradient(180deg,#c9c6c0,#5a5a5a 60%,#1e1e1e)" role="img" aria-label="Business coach speaking to a seated group">
    <svg class="service-arrow" width="22" height="22" viewBox="0 0 22 22" fill="none" stroke="#fff" stroke-width="1.5"><circle cx="11" cy="11" r="10"/><path d="M6 11h9M12 7l4 4-4 4"/></svg>
    <div class="service-title">Leadership Skills</div>
    <div class="service-text">Ut wisi enim ad minim veniam, quis nostrudexerci tation ullamcorperuscipit lobortis nisl ut aliquip</div>
  </div>
  <div class="service" style="left:403px;width:395px;background:linear-gradient(180deg,#d2ccc4,#6b7180 60%,#1f2126)" role="img" aria-label="Entrepreneurs working together in an open office">
    <svg class="service-arrow" width="22" height="22" viewBox="0 0 22 22" fill="none" stroke="#fff" stroke-width="1.5"><circle cx="11" cy="11" r="10"/><path d="M6 11h9M12 7l4 4-4 4"/></svg>
    <div class="service-title">Entrepreneurs</div>
    <div class="service-text">Ut wisi enim ad minim veniam, quis nostrudexerci tation ullamcorperuscipit lobortis nisl ut aliquip</div>
  </div>
  <div class="service" style="left:805px;width:395px;background:linear-gradient(180deg,#e6e6e4,#7b7672 60%,#222)" role="img" aria-label="Team gathered around a laptop">
    <svg class="service-arrow" width="22" height="22" viewBox="0 0 22 22" fill="none" stroke="#fff" stroke-width="1.5"><circle cx="11" cy="11" r="10"/><path d="M6 11h9M12 7l4 4-4 4"/></svg>
    <div class="service-title">Team Building</div>
    <div class="service-text">Ut wisi enim ad minim veniam, quis nostrudexerci tation ullamcorperuscipit lobortis nisl ut aliquip</div>
  </div>
</section>

<section>
  <h2 class="section-title" style="top:2161px"><span class="accent">Watch</span> <span class="hl">Videos</span></h2>
  <div class="video" style="left:0;width:593px;background:linear-gradient(180deg,#4f5a3a,#3a3b2e 60%,#111)" role="img" aria-label="Video still of the coach speaking in an office">
    <svg class="play" style="left:212px" viewBox="0 0 90 90"><circle cx="45" cy="45" r="43" fill="rgba(255,255,255,.15)" stroke="rgba(255,255,255,.6)" stroke-width="3"/><circle cx="45" cy="45" r="30" fill="rgba(0,0,0,.35)" stroke="#fff" stroke-width="2"/><path d="M38 32l18 13-18 13z" fill="#fff"/></svg>
    <div class="video-cap">Lorem ipsum dolor sit amet, consectetuer adipiscing</div>
    <div class="video-date">In January 10, 2019/ No Comment</div>
  </div>
  <div class="video" style="left:605px;width:595px;background:linear-gradient(90deg,#d9d9d6,#b9b4ae 55%,#6b3a2c);" role="img" aria-label="Video still of the coach in a red shirt presenting">
    <svg class="play" style="left:267px" viewBox="0 0 90 90"><circle cx="45" cy="45" r="43" fill="rgba(255,255,255,.15)" stroke="rgba(255,255,255,.6)" stroke-width="3"/><circle cx="45" cy="45" r="30" fill="rgba(0,0,0,.35)" stroke="#fff" stroke-width="2"/><path d="M38 32l18 13-18 13z" fill="#fff"/></svg>
    <div class="abs" style="left:0;top:180px;width:595px;height:147px;background:linear-gradient(180deg,transparent,rgba(0,0,0,.75))"></div>
    <div class="video-cap">Lorem ipsum dolor sit amet, consectetuer adipiscing</div>
    <div class="video-date">In January 10, 2019/ No Comment</div>
  </div>
  <div class="pill" style="left:537px;top:2573px;width:126px">View All <span style="margin-left:8px">⟶</span></div>
</section>

<section>
  <div class="feature" style="left:141px">
    <div class="photo" style="background:linear-gradient(180deg,#d8d8d6,#5d5d66 60%,#232430)" role="img" aria-label="Coach in a suit at a speaking event"></div>
    <div class="feature-body bg-blue"><h3>Speaking Events</h3><p>Lorem ipsum dolor sit amet,consectetuer adipiscing elit, sed diam nonummyli nibh euismod tincidunt ut laoreet dolore</p><div class="plus">+</div></div>
  </div>
  <div class="feature" style="left:451px">
    <div class="photo" style="background:linear-gradient(180deg,#e7e4de,#c9b4a0 50%,#2f62b0)" role="img" aria-label="Coach beside a whiteboard"></div>
    <div class="feature-body bg-orange"><h3>Downloadable Content</h3><p>Lorem ipsum dolor sit amet,consectetuer adipiscing elit, sed diam nonummyli nibh euismod tincidunt ut laoreet dolore</p><div class="plus">+</div></div>
  </div>
  <div class="feature" style="left:762px">
    <div class="photo" style="background:linear-gradient(180deg,#d0cfcc,#8a7d86 50%,#3b2668)" role="img" aria-label="Coach recording a podcast episode"></div>
    <div class="feature-body bg-blue"><h3>Podcast</h3><p>Lorem ipsum dolor sit amet,consectetuer adipiscing elit, sed diam nonummyli nibh euismod tincidunt ut laoreet dolore</p><div class="plus">+</div></div>
  </div>
</section>

<footer class="footer">
  <p class="footer-text">Subscribe to our newsletter to get the latest scoop right to your inbox</p>
  <div class="footer-input"><span>Your Email Address</span><b>SUBSCRIBE</b></div>
  <ul class="footer-links"><li>Home</li><li>About Us</li><li>Resources</li><li>Contact Us</li></ul>
  <svg class="contact-ico" style="top:60px" width="10" height="14" viewBox="0 0 10 14"><path d="M5 0a5 5 0 0 1 5 5c0 4-5 9-5 9S0 9 0 5a5 5 0 0 1 5-5z" fill="var(--blue)"/><circle cx="5" cy="5" r="2" fill="#1f2226"/></svg>
  <div class="contact" style="left:730px;top:58px">4821 Maple Ridge Lane<br>Ashcombe. AV 40217</div>
  <svg class="contact-ico" style="top:116px" width="11" height="11" viewBox="0 0 24 24"><path d="M5 2h4l2 5-3 2a11 11 0 0 0 6 6l2-3 5 2v4a2 2 0 0 1-2 2A17 17 0 0 1 3 4a2 2 0 0 1 2-2z" fill="var(--blue)"/></svg>
  <div class="contact" style="left:730px;top:113px">555-010-2468</div>
  <svg class="contact-ico" style="top:154px" width="12" height="9" viewBox="0 0 12 9"><rect width="12" height="9" fill="var(--blue)"/><path d="M0 0l6 5 6-5" stroke="#1f2226" fill="none"/></svg>
  <div class="contact" style="left:730px;top:151px">info@rtforguide.example</div>
  <div class="footer-brand">RT FOR GUIDE</div>
  <div class="social" style="left:937px"></div>
  <div class="social" style="left:972px"></div>
  <div class="social" style="left:1007px"></div>
  <div class="rule"></div>
  <p class="copy">Copyright © 2019 RT for Guide . All Rights Reserved.</p>
</footer>

</body>
</html>
```